Wine Bottle Label for the brand Gliding Heron for a Sherry wine

A wine label for a Dry Sherry. We want it consistent with existing Gliding Heron and Quiet Otter labeling. It should say "Quiet Otter Sherry" We want a very retro look similar to the attached labels which are from our core wines. The sherry is a side project that fits into the 'quiet otter' series (label included). We would like a lot of the similar label structure to the existing quiet otter label, but with a different caricature of the fox. We have had one that we did in Copper ridge bourbon barrels and the caricature was of a buffalo with a barrel imbibing. We have also had a giraffe on a skin contact white. I have included the mural and other logos throughout the project to give you a sense of the previous work we have done.

Industry/Entity Type

Winemaking, wine labels

Requirements
Must have
• Quiet Otter elements

```html
<!DOCTYPE html>
<html lang="en">
<head>
<meta charset="utf-8">
<title>Gliding Heron – Quiet Otter Sherry Label</title>
<link rel="stylesheet" href="https://fonts.googleapis.com/css2?family=Anton&family=Archivo+Black&display=swap">
<style>
  :root {
    --page: #ffffff;
    --halo: #fdf9dc;
    --label-cream: #f9f0a8;
    --label-cream-soft: #fdf8d6;
    --frame-red: #e94d40;
    --brand-orange: #f04a25;
    --title-red: #e8483f;
    --vine-green: #c9c98a;
    --vine-plum: #6b2a3c;
  }
  html, body {
    margin: 0;
    padding: 0;
    width: 1094px;
    height: 1200px;
    overflow: hidden;
    background: var(--page);
  }
  .canvas {
    position: relative;
    width: 1094px;
    height: 1200px;
  }
  .label-art {
    position: absolute;
    inset: 0;
  }
  .brand-name text {
    font-family: "Archivo Black", "Arial Black", sans-serif;
    fill: var(--brand-orange);
  }
  .product-name text {
    font-family: "Anton", "Impact", sans-serif;
    fill: var(--title-red);
  }
  .vine-illustration {
    position: absolute;
    left: 315px;
    top: 469px;
    width: 448px;
    height: 216px;
    border-radius: 60px 60px 140px 140px;
    background: radial-gradient(ellipse at 50% 40%, #dcd69a 0%, #c4b47e 45%, rgba(107, 42, 60, 0.45) 100%);
  }
</style>
</head>
<body>
  <main class="canvas">
    <svg class="label-art" width="1094" height="1200" viewBox="0 0 1094 1200">
      <defs>
        <radialGradient id="label-paper" cx="50%" cy="45%" r="70%">
          <stop offset="0%" stop-color="var(--label-cream-soft)"/>
          <stop offset="70%" stop-color="var(--label-cream)"/>
          <stop offset="100%" stop-color="#f4e89a"/>
        </radialGradient>
        <radialGradient id="label-halo" cx="50%" cy="50%" r="55%">
          <stop offset="80%" stop-color="var(--halo)"/>
          <stop offset="100%" stop-color="var(--page)"/>
        </radialGradient>
      </defs>

      <rect class="label-halo" x="96" y="72" width="906" height="1098" rx="80" fill="url(#label-halo)"/>

      <path class="label-body"
        d="M177,100 H920 A54,54 0 0 0 974,154 V1087 A54,54 0 0 0 920,1141 H177 A54,54 0 0 0 123,1087 V154 A54,54 0 0 0 177,100 Z"
        fill="url(#label-paper)" stroke="var(--frame-red)" stroke-width="15"/>

      <g class="brand-name" aria-label="Gliding Heron">
        <text x="545" y="300" font-size="104" text-anchor="middle" textLength="500" lengthAdjust="spacingAndGlyphs">GLIDING</text>
        <text x="547" y="420" font-size="104" text-anchor="middle" textLength="420" lengthAdjust="spacingAndGlyphs">HERON</text>
      </g>

      <g class="product-name" aria-label="Quiet Otter Sherry">
        <text x="547" y="840" font-size="104" text-anchor="middle" textLength="675" lengthAdjust="spacingAndGlyphs">Quiet Otter Sherry</text>
      </g>
    </svg>

    <div class="vine-illustration" role="img" aria-label="Engraved grape vine with two hanging bunches of grapes and leaves"></div>
  </main>
</body>
</html>
```